Dating Coach needs a Book Cover Design

My new book called "Where the Lanterns Gather: Meeting Someone Worth Knowing in a Crowded Digital Age" needs a cover! I tried to make one on my own, but it's just not my skill set :) Please see attached for my best attempt. I'd like to see the title smaller and the tagline bigger - so that the tagline is easier to read. But I'm not sure how to do this and still have the Title look great. I'm also considering if the "WHERE LANTERNS GATHER" part should not be in all caps. Looking forward to your ideas! I'm also afraid that the drawing is a bit too cartoonish and doesn't match my brand. I'm looking for something elegant and also very approachable and down to earth. My website is www.gretavondlecounsel.example so you can use as reference! Please see my attached brand style guide for colors. This will be an e-book that I give away for free to anyone who signs up for my newsletter. Some mock-ups would also be great to use in advertising.

```html
<!DOCTYPE html>
<html lang="en">
<head>
<meta charset="UTF-8">
<title>Where the Lanterns Gather — Book Cover</title>
<link href="https://fonts.googleapis.com/css2?family=Cormorant+Garamond:wght@500;600&family=Nunito:wght@400&family=Montserrat:wght@600&display=swap" rel="stylesheet">
<style>
  :root {
    --page-bg: #efe7dc;
    --cover-cream: #f6efe4;
    --cover-cream-deep: #ebdfce;
    --title-purple: #4a2f63;
    --tagline-purple: #5a3f74;
    --accent-gold: #a8863f;
    --hay-light: #d9c29a;
    --hay-mid: #b99a63;
    --hay-deep: #8f7444;
  }
  * { margin: 0; padding: 0; box-sizing: border-box; }
  html, body {
    width: 1200px;
    height: 960px;
    overflow: hidden;
    background: var(--page-bg);
  }
  .stage {
    width: 1200px;
    height: 960px;
    display: flex;
    align-items: center;
    justify-content: center;
  }
  .book-cover {
    position: relative;
    width: 540px;
    height: 900px;
    background: radial-gradient(ellipse at 50% 30%, var(--cover-cream) 0%, var(--cover-cream-deep) 100%);
    overflow: hidden;
    text-align: center;
  }
  .ornament-rule {
    position: absolute;
    left: 90px;
    width: 360px;
    height: 30px;
  }
  .ornament-rule--top { top: 62px; }
  .ornament-rule--bottom { top: 364px; }
  .title {
    position: absolute;
    top: 100px;
    left: 0;
    width: 100%;
    font-family: "Cormorant Garamond", Georgia, serif;
    font-weight: 500;
    color: var(--title-purple);
    line-height: 1;
  }
  .title__lead {
    display: block;
    font-size: 46px;
    margin-bottom: 10px;
  }
  .title__main {
    display: block;
    font-size: 92px;
    line-height: 0.95;
  }
  .tagline {
    position: absolute;
    top: 408px;
    left: 50px;
    width: 440px;
    font-family: "Nunito", Arial, sans-serif;
    font-weight: 400;
    font-size: 33px;
    line-height: 1.4;
    color: var(--tagline-purple);
  }
  .cover-art {
    position: absolute;
    top: 520px;
    left: 0;
    width: 100%;
    height: 320px;
    background:
      radial-gradient(ellipse at 50% 55%, var(--hay-mid) 0%, var(--hay-light) 45%, rgba(217,194,154,0) 80%),
      linear-gradient(to bottom, rgba(246,239,228,0) 0%, var(--hay-light) 35%, var(--hay-deep) 70%, rgba(235,223,206,0.9) 100%);
  }
  .author {
    position: absolute;
    bottom: 28px;
    left: 0;
    width: 100%;
    font-family: "Montserrat", Arial, sans-serif;
    font-weight: 600;
    font-size: 28px;
    letter-spacing: 0.2em;
    color: var(--accent-gold);
  }
</style>
</head>
<body>
  <main class="stage">
    <section class="book-cover">
      <svg class="ornament-rule ornament-rule--top" viewBox="0 0 360 30" aria-hidden="true">
        <line x1="0" y1="15" x2="150" y2="15" stroke="var(--accent-gold)" stroke-width="1.5"/>
        <line x1="210" y1="15" x2="360" y2="15" stroke="var(--accent-gold)" stroke-width="1.5"/>
        <path d="M180 25 C165 15 164 5 172 4 C177 3 180 8 180 10 C180 8 183 3 188 4 C196 5 195 15 180 25 Z" fill="none" stroke="var(--accent-gold)" stroke-width="1.5"/>
      </svg>

      <h1 class="title">
        <span class="title__lead">Where the</span>
        <span class="title__main">Lanterns</span>
        <span class="title__main">Gather</span>
      </h1>

      <svg class="ornament-rule ornament-rule--bottom" viewBox="0 0 360 30" aria-hidden="true">
        <line x1="0" y1="15" x2="150" y2="15" stroke="var(--accent-gold)" stroke-width="1.5"/>
        <line x1="210" y1="15" x2="360" y2="15" stroke="var(--accent-gold)" stroke-width="1.5"/>
        <path d="M180 25 C165 15 164 5 172 4 C177 3 180 8 180 10 C180 8 183 3 188 4 C196 5 195 15 180 25 Z" fill="none" stroke="var(--accent-gold)" stroke-width="1.5"/>
      </svg>

      <p class="tagline">Meeting someone worth knowing in a crowded digital age</p>

      <div class="cover-art" role="img" aria-label="Photograph of a soft lavender felt heart resting in a nest of golden straw"></div>

      <p class="author">GRETA VONDLE</p>
    </section>
  </main>
</body>
</html>
```